Personal letterhead and stationary

I am looking for someone to design letterhead and stationary set for my personal use. I want something simple and timeless with a little bit of color. I like photography, computers and writing.

```html
<!DOCTYPE html>
<html lang="en">
<head>
<meta charset="utf-8">
<title>Thomas Adam Hartley — Personal Stationery</title>
<link href="https://fonts.googleapis.com/css2?family=Josefin+Slab:wght@400;600&display=swap" rel="stylesheet">
<style>
  :root {
    --backdrop: #000000;
    --paper: #ffffff;
    --ink: #1a1a1a;
    --rule: #8a8a8a;
    --rule-light: #c8c8c8;
    --shadow: rgba(0,0,0,0.45);
  }
  * { box-sizing: border-box; margin: 0; padding: 0; }
  html, body { width: 850px; height: 1200px; overflow: hidden; background: var(--backdrop); }
  body { position: relative; font-family: "Josefin Slab", Georgia, serif; color: var(--ink); }

  .sheet { position: absolute; background: var(--paper); }

  /* Letterhead */
  .letterhead { left: 161px; top: 83px; width: 606px; height: 855px; }
  .letterhead .name { position: absolute; left: 60px; top: 77px; font-size: 14px; letter-spacing: 0; white-space: nowrap; }
  .letterhead .email { position: absolute; left: 60px; top: 107px; font-size: 9px; white-space: nowrap; }
  .letterhead .phone { position: absolute; right: 54px; top: 76px; font-size: 13px; display: flex; align-items: center; gap: 5px; white-space: nowrap; }
  .letterhead .address { position: absolute; right: 55px; top: 107px; font-size: 9px; white-space: nowrap; }
  .letterhead .header-rule { position: absolute; top: 100px; height: 5px; border-top: 1px solid var(--ink); border-bottom: 1px solid var(--ink); }
  .letterhead .header-rule.left { left: 59px; width: 198px; }
  .letterhead .header-rule.right { left: 351px; width: 199px; }
  .letterhead .footer-rule { position: absolute; left: 0; top: 816px; width: 558px; border-top: 1px solid var(--rule-light); }

  .seal { position: absolute; display: flex; align-items: center; justify-content: center; border-radius: 50%; border: 1.5px solid var(--ink); background: var(--paper); font-weight: 600; letter-spacing: 0.5px; color: var(--ink); }
  .letterhead .seal { left: 258px; top: 56px; width: 94px; height: 94px; font-size: 13px; }

  /* Envelope front */
  .envelope-front { left: 67px; top: 667px; width: 508px; height: 239px; box-shadow: 6px 7px 6px var(--shadow); border: 1px solid var(--rule-light); }
  .envelope-front .side-rule { position: absolute; left: 69px; top: 0; width: 7px; height: 100%; border-left: 1px solid var(--rule); border-right: 1px solid var(--rule); }
  .envelope-front .seal { left: 46px; top: 28px; width: 52px; height: 52px; font-size: 8px; }
  .envelope-front .name { position: absolute; left: 91px; top: 86px; font-size: 12px; letter-spacing: 0.8px; white-space: nowrap; }
  .envelope-front .address { position: absolute; left: 91px; top: 104px; font-size: 10px; white-space: nowrap; }
  .envelope-front .stamp { position: absolute; left: 455px; top: 14px; width: 38px; height: 44px; border: 1px solid var(--rule-light); }
  .envelope-front .contact { position: absolute; right: 12px; top: 202px; text-align: right; font-size: 8px; line-height: 1.7; white-space: nowrap; }
  .envelope-front .contact .email { font-size: 10px; }

  /* Envelope back */
  .envelope-back { left: 64px; top: 922px; width: 510px; height: 241px; border: 1px solid var(--rule-light); }
  .envelope-back .flap-line { position: absolute; left: 0; top: 71px; width: 100%; height: 22px; border-top: 1px solid var(--rule-light); background: linear-gradient(#f0f0f0, var(--paper)); }
  .envelope-back .seal { left: 230px; top: 46px; width: 50px; height: 50px; font-size: 8px; }
</style>
</head>
<body>

<section class="sheet letterhead" aria-label="Letterhead">
  <div class="name">THOMAS ADAM HARTLEY</div>
  <div class="email">thomas@postbox.example</div>
  <div class="header-rule left"></div>
  <div class="header-rule right"></div>
  <div class="seal">HARTLEY</div>
  <div class="phone">
    <svg width="10" height="12" viewBox="0 0 10 12" aria-hidden="true"><path d="M3 0.5 L4.5 3.5 L3.2 4.6 C3.8 6.5 5 8 6.4 9 L7.6 8 L9.6 10 C8.8 11.2 7.8 11.6 6.8 11.3 C3.5 9.8 1 6.5 0.6 3 C0.6 1.8 1.5 0.9 3 0.5 Z" fill="#1a1a1a"/></svg>
    <span>041250736918</span>
  </div>
  <div class="address">14 elm st baxterfield vic 4210</div>
  <div class="footer-rule"></div>
</section>

<section class="sheet envelope-front" aria-label="Envelope front">
  <div class="side-rule"></div>
  <div class="seal">HARTLEY</div>
  <div class="name">THOMAS ADAM HARTLEY</div>
  <div class="address">14 elm st baxterfield vic 4210</div>
  <div class="stamp"></div>
  <div class="contact">
    <div>041250736918</div>
    <div class="email">thomas@postbox.example</div>
  </div>
</section>

<section class="sheet envelope-back" aria-label="Envelope back">
  <div class="flap-line"></div>
  <div class="seal">HARTLEY</div>
</section>

</body>
</html>
```